2018 Desk Calendar Design with Better Spine, Better Health with Chiropractic

In conjunction with the Federation of Vertebral Wellness Malaysia (FVW), we are organizing a 2018 desk calendar design. The cover page and monthly design size is 210mm (H) x 195mm (W). The will be a total of 27 designs including a cover page (front) [Sample 1], cover page (back) Malaysia National & States Holiday 2018 (https://calendaroffdays.com.my/2018-dates/) [Sample 2], 12 months design (front) [Sample 3 and 4], 12 months design (back) [Sample 5], Last page (2017 and 2019 calendar) [Sample 6].

Below are some recommendations for monthly back cover design. The main theme remain as Better SPINE, Better HEALTH with CHIROPRACTIC. Each month can in collaborate with of the following element:-

Suggestion 1 (Celebration of the Month)
January - New Year
February - Chinese New Year
March -
April -
May - Labour Day
June - Aidilfitri Festival
July-
August - Independent Day
September - Malaysia Day
October - Global Posture Week
November - Deepavali Festival
December - Christmas

Suggestion 2 (States in Malaysia)
January - Perlis
February - Kedah
March - Penang
April - Perak
May - Selangor
June - Negeri Sembilan
July- Melaka
August - Johor
September - Pahang
October - Terengganu
November - Kelantan
December - Sabah & Sarawak

Reason: Looking forward to receive all the designs.

Target Market(s)

Chiropractors and Public

Industry/Entity Type

Chiropractor

Colors

Designer to choose colors to be used in the design.

Requirements
Must have
• The theme for the desk calendar design is Better Spine, Better Health with Chiropractic.
• The cover page should include 5th Anniversary element.
Nice to have
• Lunar or Islamic calendar is optional in the Gregorian calendar.
• AI Format
• Footnote of each page www.vertifvw.org

```html
<!DOCTYPE html>
<html lang="en">
<head>
<meta charset="utf-8">
<title>October 2018 – FVW Desk Calendar</title>
<link rel="stylesheet" href="https://fonts.googleapis.com/css2?family=Michroma&family=Orbitron:wght@600;700&family=Rokkitt:wght@400&family=Arimo&display=swap">
<style>
  :root {
    --paper: #dcbaa8;
    --red: #e8392a;
    --red-soft: #e64a36;
    --band-dark: #a94c3b;
    --band-light: #d9957e;
    --ink: #111111;
    --photo-light: #f1f1f0;
    --photo-mid: #d8d6d4;
    --photo-warm: #b9a493;
    --mark-blue: #2a3d8f;
  }
  * { margin: 0; padding: 0; box-sizing: border-box; }
  html, body { width: 1104px; height: 1200px; overflow: hidden; background: var(--paper); }
  .page {
    position: relative;
    width: 1104px;
    height: 1200px;
    background: var(--paper);
    overflow: hidden;
    font-family: "Orbitron", sans-serif;
    color: var(--ink);
  }
  .artwork { position: absolute; inset: 0; width: 1104px; height: 1200px; }

  .spine-fact {
    position: absolute;
    left: 376px;
    top: 40px;
    font-family: "Rokkitt", serif;
    font-weight: 400;
    font-size: 32px;
    line-height: 39px;
    color: var(--red);
    letter-spacing: 0.5px;
  }

  .mini-month { position: absolute; left: 22px; top: 308px; }
  .mini-month__title {
    font-family: "Michroma", sans-serif;
    font-size: 17px;
    letter-spacing: 2px;
    margin-left: 44px;
    margin-bottom: 14px;
    text-transform: uppercase;
  }
  .mini-month__grid {
    display: grid;
    grid-template-columns: 32px 40px 35px 38px 37px 36px 36px;
    row-gap: 12px;
    font-size: 14px;
    font-weight: 700;
  }
  .mini-month__grid span { height: 19px; line-height: 19px; }

  .month-title {
    position: absolute;
    left: 96px;
    top: 540px;
    font-family: "Michroma", sans-serif;
    font-size: 54px;
    letter-spacing: 12px;
    color: var(--red);
    line-height: 1;
    white-space: nowrap;
  }
  .month-title .initial { font-size: 65px; }

  .anniversary-mark {
    position: absolute;
    left: 600px;
    top: 562px;
    display: flex;
    align-items: center;
    gap: 8px;
    font-family: "Orbitron", sans-serif;
    font-weight: 700;
    font-size: 24px;
    color: var(--mark-blue);
  }
  .anniversary-mark__dot {
    width: 22px; height: 22px; border-radius: 50%;
    background: var(--mark-blue);
  }

  .calendar { position: absolute; left: 101px; top: 646px; }
  .weekdays, .week {
    display: grid;
    grid-template-columns: 121px 129px 130px 130px 127px 132px 129px;
    padding-left: 8px;
    font-weight: 700;
  }
  .weekdays { font-size: 28px; line-height: 30px; height: 89px; }
  .weeks { display: flex; flex-direction: column; gap: 39px; }
  .week {
    width: 906px;
    height: 56px;
    padding-top: 15px;
    font-size: 30px;
    line-height: 31px;
    border-bottom: 2px solid var(--red);
  }
  .week--short { width: 389px; }
  .sun { color: var(--red); }

  .site {
    position: absolute;
    right: 18px;
    bottom: 14px;
    font-family: "Arimo", sans-serif;
    font-size: 20px;
    color: var(--ink);
  }
</style>
</head>
<body>
<main class="page">
  <svg class="artwork" viewBox="0 0 1104 1200">
    <defs>
      <linearGradient id="photoTone" x1="0" y1="0" x2="1" y2="0.3">
        <stop offset="0" stop-color="#f1f1f0"/>
        <stop offset="0.55" stop-color="#d8d6d4"/>
        <stop offset="1" stop-color="#b9a493"/>
      </linearGradient>
    </defs>
    <path role="img" aria-label="Photo of a smiling woman eating a forkful of fresh salad"
          d="M120 0 H1104 V600 C1010 520 900 450 760 400 C580 330 470 220 330 140 C250 90 180 40 120 0 Z"
          fill="url(#photoTone)"/>
    <g class="spine-band">
      <path d="M0 70 C200 110 340 220 480 300 C640 390 820 410 960 500 C1040 550 1080 620 1104 720 V760 C1070 660 1030 600 950 550 C800 460 620 440 460 350 C320 270 190 150 0 130 Z"
            fill="var(--band-light)"/>
      <path d="M0 95 C200 125 340 235 480 320 C640 405 820 425 960 515 C1040 565 1080 630 1104 730 V745 C1070 650 1030 590 950 540 C810 455 630 430 470 340 C330 260 200 150 0 115 Z"
            fill="var(--band-dark)"/>
    </g>
    <path role="img" aria-label="Illustration of red vertebrae running down a curved spine"
          d="M20 20 C160 80 280 200 420 290 C580 390 760 380 900 460 C1020 530 1080 610 1110 700"
          fill="none" stroke="var(--red-soft)" stroke-width="62" stroke-linecap="round"/>
  </svg>

  <p class="spine-fact">Spine Fact:<br>October 16th is<br>Global Posture Week</p>

  <section class="mini-month" aria-label="September 2018">
    <h2 class="mini-month__title">September</h2>
    <div class="mini-month__grid">
      <span>M</span><span>T</span><span>W</span><span>T</span><span>F</span><span>S</span><span class="sun">S</span>
      <span></span><span></span><span></span><span></span><span></span><span>1</span><span class="sun">2</span>
      <span>3</span><span>4</span><span>5</span><span>6</span><span>7</span><span>8</span><span class="sun">9</span>
      <span>10</span><span>11</span><span>12</span><span>13</span><span>14</span><span>15</span><span class="sun">16</span>
      <span>17</span><span>18</span><span>19</span><span>20</span><span>21</span><span>22</span><span class="sun">23</span>
      <span>24</span><span>25</span><span>26</span><span>27</span><span>28</span><span>29</span><span class="sun">30</span>
    </div>
  </section>

  <h1 class="month-title"><span class="initial">O</span>CTOBER</h1>

  <div class="anniversary-mark"><span class="anniversary-mark__dot"></span>FVW</div>

  <section class="calendar" aria-label="October 2018">
    <div class="weekdays">
      <span>M</span><span>T</span><span>W</span><span>T</span><span>F</span><span>S</span><span class="sun">S</span>
    </div>
    <div class="weeks">
      <div class="week"><span>1</span><span>2</span><span>3</span><span>4</span><span>5</span><span>6</span><span class="sun">7</span></div>
      <div class="week"><span>8</span><span>9</span><span>10</span><span>11</span><span>12</span><span>13</span><span class="sun">14</span></div>
      <div class="week"><span>15</span><span>16</span><span>17</span><span>18</span><span>19</span><span>20</span><span class="sun">21</span></div>
      <div class="week"><span>22</span><span>23</span><span>24</span><span>25</span><span>26</span><span>27</span><span class="sun">28</span></div>
      <div class="week week--short"><span>29</span><span>30</span><span>31</span></div>
    </div>
  </section>

  <p class="site">www.vertifvw.org</p>
</main>
</body>
</html>
```